Certified Public Accountant specializing in tax preparation.

I need a business card designed that conveys knowledgeability, trustworthiness and competency. I am a licensed CPA and hold a Master's in taxation. As this is a personal service business, I would like to include my picture on the card.

```html
<!DOCTYPE html>
<html lang="en">
<head>
<meta charset="utf-8">
<title>Maren Hollis – Business Card</title>
<link href="https://fonts.googleapis.com/css2?family=Questrial&display=swap" rel="stylesheet">
<style>
  :root {
    --stage: #e6e8ea;
    --card: #ffffff;
    --ink: #111111;
    --accent-red: #e8463f;
    --accent-teal: #1f9aa6;
    --pattern-blue: #bfe3f1;
    --pattern-blue-soft: #e3f3f9;
    --photo-pink: #e9b8cf;
    --photo-hair: #5a3a2c;
    --photo-light: #f6eef1;
  }
  * { margin: 0; padding: 0; box-sizing: border-box; }
  html, body {
    width: 1200px; height: 902px; overflow: hidden;
    background: var(--stage);
    font-family: "Questrial", "Century Gothic", sans-serif;
  }
  .card {
    position: absolute; left: 100px; top: 165px;
    width: 1000px; height: 572px;
    background: var(--card);
    overflow: hidden;
    box-shadow: 0 12px 30px rgba(0,0,0,0.18);
  }
  .card-pattern {
    position: absolute; inset: 0;
    background:
      radial-gradient(ellipse 60% 45% at 10% 100%, var(--pattern-blue) 0%, var(--pattern-blue-soft) 55%, transparent 100%),
      radial-gradient(ellipse 55% 40% at 30% 0%, var(--pattern-blue) 0%, var(--pattern-blue-soft) 50%, transparent 100%),
      radial-gradient(ellipse 35% 35% at 60% 90%, var(--pattern-blue-soft) 0%, transparent 100%);
  }
  .portrait {
    position: absolute; right: 0; top: 0;
    width: 460px; height: 572px;
    background:
      radial-gradient(ellipse 30% 32% at 45% 22%, var(--photo-hair) 0%, rgba(90,58,44,0.6) 60%, transparent 100%),
      radial-gradient(ellipse 60% 45% at 55% 85%, var(--photo-pink) 0%, rgba(233,184,207,0.7) 60%, transparent 100%),
      linear-gradient(to right, rgba(255,255,255,0) 0%, var(--photo-light) 35%, var(--photo-light) 100%);
    -webkit-mask-image: linear-gradient(to right, transparent 0%, #000 30%);
            mask-image: linear-gradient(to right, transparent 0%, #000 30%);
  }
  .identity { position: absolute; left: 66px; top: 118px; width: 470px; }
  .name {
    font-size: 66px; line-height: 1; color: var(--ink);
    letter-spacing: 0.5px; font-weight: 400;
  }
  .title-row {
    display: flex; align-items: center; gap: 10px;
    margin-top: 6px;
  }
  .title-row .rule { flex: 1; height: 2px; background: var(--accent-red); }
  .title {
    color: var(--accent-red); font-size: 24px; letter-spacing: 1.5px;
  }
  .company {
    margin-top: 4px; font-size: 44px; line-height: 1;
    color: var(--ink); letter-spacing: 1px; text-transform: uppercase;
  }
  .credentials {
    margin-top: 8px; font-size: 23px; color: var(--accent-teal);
    letter-spacing: 0.6px;
  }
  .contact {
    position: absolute; left: 66px; top: 376px;
    font-size: 23px; line-height: 30px; color: var(--ink);
    letter-spacing: 0.5px;
  }
  .address { margin-bottom: 14px; }
  .contact .label { color: var(--accent-red); }
</style>
</head>
<body>
  <section class="card">
    <div class="card-pattern"></div>
    <div class="portrait" role="img" aria-label="Portrait photo of the accountant in a pink blazer with arms crossed"></div>

    <div class="identity">
      <h1 class="name">Maren Hollis</h1>
      <div class="title-row">
        <span class="rule"></span>
        <span class="title">PRESIDENT</span>
        <span class="rule"></span>
      </div>
      <p class="company">Clearpath Tax</p>
      <p class="credentials">Certified Public Accountant, MAcc</p>
    </div>

    <div class="contact">
      <p class="address">240 W. Orchard Lane<br>Suite B, Linden, CA 90415</p>
      <p><span class="label">P:</span> 555.014.2286</p>
      <p><span class="label">F:</span> 555.014.7731</p>
      <p><span class="label">E:</span> hello@marenhollis.com</p>
    </div>
  </section>
</body>
</html>
```